Lotus Leaf Kitchen Road Billboard

Road Billboard I need all of this information on it
Authentic Thai Food Bangkok Style
6.5 Miles on the right
4126 Maple Ridge Rd Otto NC
828-555-4172

```html
<!DOCTYPE html>
<html lang="en">
<head>
<meta charset="utf-8">
<title>Lotus Leaf Kitchen – Road Billboard</title>
<link rel="stylesheet" href="https://fonts.googleapis.com/css2?family=Archivo+Black&family=Roboto:wght@700;900&family=Roboto+Condensed:wght@400;700&display=swap">
<style>
  :root {
    --page: #d0d0d0;
    --ink: #0b0b0b;
    --gold: #d6a812;
    --gold-deep: #b88c0a;
    --arrow: #e8e8e8;
    --paper: #f2f2f2;
    --ember: #e07a1c;
    --flame: #f6b23c;
    --leaf: #5f7a2a;
  }
  * { margin: 0; padding: 0; box-sizing: border-box; }
  html, body { width: 1200px; height: 690px; overflow: hidden; background: var(--page); }
  .canvas { position: relative; width: 1200px; height: 690px; }
  .billboard {
    position: absolute; left: 67px; top: 67px; width: 1067px; height: 556px;
    overflow: hidden; box-shadow: 14px 16px 22px rgba(0,0,0,0.35);
    background: var(--ink);
  }
  .hero-photo {
    position: absolute; inset: 0;
    background:
      radial-gradient(ellipse 32% 45% at 22% 42%, rgba(246,178,60,0.9), rgba(224,122,28,0.45) 55%, transparent 80%),
      radial-gradient(ellipse 28% 40% at 50% 30%, rgba(120,150,70,0.55), transparent 75%),
      radial-gradient(ellipse 50% 25% at 55% 72%, rgba(60,55,45,0.9), transparent 80%),
      linear-gradient(100deg, #090909 0%, #151310 40%, #4a4418 80%, #8a7a1a 100%);
  }
  .brand {
    position: absolute; left: 770px; top: 130px; display: flex; align-items: center; gap: 10px;
    font-family: "Roboto Condensed", sans-serif; font-weight: 700; font-size: 24px; color: #ffffff;
  }
  .brand-dot { width: 14px; height: 14px; border-radius: 50%; background: #ffffff; }
  .shapes, .headline { position: absolute; left: 0; top: 0; }
  .headline text {
    font-family: "Archivo Black", sans-serif; fill: var(--gold);
    stroke: var(--paper); stroke-width: 2px; paint-order: stroke;
  }
  .headline .shadow { fill: var(--ink); stroke: var(--ink); stroke-width: 3px; }
  .distance {
    position: absolute; left: 476px; top: 436px; white-space: nowrap; color: var(--ink);
    display: flex; align-items: baseline; gap: 12px;
  }
  .distance-miles { font-family: "Roboto", sans-serif; font-weight: 900; font-size: 50px; letter-spacing: -0.5px; }
  .distance-side { font-family: "Roboto Condensed", sans-serif; font-weight: 400; font-size: 36px; }
  .address {
    position: absolute; left: 476px; top: 502px; display: flex; align-items: center; gap: 18px;
    font-family: "Roboto Condensed", sans-serif; font-weight: 700; font-size: 31px; color: var(--gold);
    white-space: nowrap;
  }
  .phone {
    position: absolute; left: 32px; top: 503px; display: flex; align-items: center; gap: 16px;
    font-family: "Roboto Condensed", sans-serif; font-weight: 700; font-size: 37px; color: var(--paper);
  }
</style>
</head>
<body>
<div class="canvas">
  <section class="billboard">
    <div class="hero-photo" role="img" aria-label="Photo of a flaming wok tossing shrimp, broccoli and vegetables with sparks"></div>

    <div class="brand"><span class="brand-dot"></span><span class="brand-name">Lotus Leaf Kitchen</span></div>

    <svg class="shapes" width="1067" height="556" viewBox="0 0 1067 556">
      <rect class="bottom-band" x="0" y="490" width="1067" height="66" fill="var(--ink)"/>
      <polygon class="phone-band" points="0,491 393,491 330,556 0,556" fill="var(--gold)"/>
      <polygon class="direction-arrow" points="395,490 440,432 954,432 954,399 1067,462 954,524 954,490" fill="var(--arrow)"/>
    </svg>

    <svg class="headline" width="1067" height="556" viewBox="0 0 1067 556">
      <text class="shadow" x="104" y="279" font-size="86" textLength="866" lengthAdjust="spacingAndGlyphs">AUTHENTIC THAI FOOD</text>
      <text x="100" y="275" font-size="86" textLength="866" lengthAdjust="spacingAndGlyphs">AUTHENTIC THAI FOOD</text>
      <text class="shadow" x="279" y="346" font-size="64" textLength="513" lengthAdjust="spacingAndGlyphs">BANGKOK STYLE</text>
      <text x="275" y="342" font-size="64" textLength="513" lengthAdjust="spacingAndGlyphs">BANGKOK STYLE</text>
    </svg>

    <div class="distance"><span class="distance-miles">6.5 Miles</span><span class="distance-side">ON THE RIGHT</span></div>

    <div class="address">
      <svg width="32" height="32" viewBox="0 0 32 32" aria-hidden="true">
        <path d="M10 2a7 7 0 0 1 7 7c0 5-7 12-7 12S3 14 3 9a7 7 0 0 1 7-7z" fill="var(--gold)"/>
        <circle cx="10" cy="9" r="2.6" fill="var(--ink)"/>
        <path d="M2 30 L8 20 L18 24 L30 20 L30 30 Z" fill="var(--gold)"/>
      </svg>
      <span>4126 MAPLE RIDGE RD OTTO NC</span>
    </div>

    <div class="phone">
      <svg width="40" height="26" viewBox="0 0 40 26" aria-hidden="true">
        <path d="M2 9c0-5 8-7 18-7s18 2 18 7v3h-9V8H11v4H2z" fill="var(--paper)"/>
        <path d="M9 13h22l5 12H4z" fill="var(--paper)"/>
        <circle cx="20" cy="18" r="3.5" fill="var(--gold)"/>
      </svg>
      <span>828-555-4172</span>
    </div>
  </section>
</div>
</body>
</html>
```